Coral Pillow Depot Website

Need a design for a local Miami mattress store.
The store is called Coral Pillow Depot.
need it to be something that customers can find on the internet and will
give them my location, they need to know i have the same brand mattress as the other store except i have them at almost half the price.

the office phone number is (786)555-0147
the office address is: 4721 sw Heron Glade Ave, Miami FL 33190

included is the logo, id like to stick the with white and teal design

here are is an excerpt that can or cannot be included

"We are a premium mattress discount outlet store located in South Florida; offering Free Delivery to Broward Miami-Dade, the Keys, and Palm Beach.

We carry the best brands in the market: Harlow DreamNest; Brovik SpineEase, Kendal & Pryce, Tarvin, among others.

We are open 7 days a week, and we are accessible from all major highways. We are a family business and our goal is to provide you with the most comfortable and best quality mattress at a price that has no competition. Come visit us and take a look at our large inventory selection."

```html
<!DOCTYPE html>
<html lang="en">
<head>
<meta charset="utf-8">
<title>Coral Pillow Depot</title>
<link href="https://fonts.googleapis.com/css2?family=Lato:wght@400;700;900&family=Playfair+Display:ital,wght@0,400;1,400;1,700&display=swap" rel="stylesheet">
<style>
:root{
  --teal:#2bb3c0;
  --teal-dark:#1f8f9a;
  --ink:#333333;
  --muted:#777777;
  --line:#d8d8d8;
  --paper:#ffffff;
  --mist:#ececec;
  --sand:#efe9dc;
  --sand-dark:#cdbf9f;
  --orange:#e8742a;
  --charcoal:#444444;
  --footer-bar:#5b5b5b;
}
*{box-sizing:border-box;margin:0;padding:0}
html,body{width:1200px;height:2352px;overflow:hidden}
body{position:relative;background:var(--paper);font-family:'Lato',sans-serif;color:var(--ink)}
.abs{position:absolute}

/* top bar */
.topbar{left:0;top:0;width:1200px;height:48px;background:var(--teal)}
.social{left:144px;top:12px;display:flex;gap:8px}
.social span{width:24px;height:24px;background:rgba(255,255,255,.9);border-radius:3px;display:block}
.account{right:170px;top:14px;display:flex;gap:20px;color:#fff;font-size:16px;font-weight:700}
.search{right:40px;top:10px;width:120px;height:28px;background:#fff;border-radius:3px;display:flex;align-items:center;padding-left:8px;font-size:12px;color:#999}
.search b{position:absolute;right:0;top:0;width:28px;height:28px;background:var(--teal-dark);border-radius:0 3px 3px 0}

/* logo */
.brand{left:0;top:120px;width:1200px;text-align:center}
.brand-dot{display:inline-block;width:18px;height:18px;border-radius:50%;background:var(--teal);vertical-align:middle;margin-right:14px}
.brand-name{font-family:'Playfair Display',serif;font-size:50px;color:var(--charcoal);vertical-align:middle}

/* nav */
.nav{left:0;top:258px;width:1200px;height:44px;border-top:2px solid var(--line);border-bottom:2px solid var(--line);display:flex;justify-content:center;gap:34px;align-items:center;font-size:24px;color:var(--muted)}
.nav .active{color:var(--teal);border-bottom:3px solid var(--teal);padding-bottom:2px}

/* hero */
.hero{left:0;top:312px;width:1200px;height:376px;background:linear-gradient(100deg,#5b4a3e 0%,#a79482 35%,#d7cfc4 55%,#6f665e 100%)}
.hero-copy{left:840px;top:350px;width:320px;color:#fff;font-size:28px;line-height:34px;text-shadow:0 1px 3px rgba(0,0,0,.5)}
.btn-shop{left:900px;top:510px;width:150px;height:46px;background:var(--sand-dark);color:#333;font-size:22px;font-weight:700;border-radius:4px;display:flex;align-items:center;justify-content:center}
.arrow{width:40px;height:40px}
.dots{left:560px;top:648px;display:flex;gap:8px}
.dots span{width:14px;height:14px;border-radius:50%;background:#bbb}
.dots span.on{background:var(--teal)}

/* featured */
.featured{left:0;top:688px;width:1200px;height:512px;background:var(--mist)}
.section-title{width:1200px;left:0;text-align:center;font-family:'Playfair Display',serif;font-style:italic;font-weight:700;font-size:46px;color:var(--ink)}
.rule{height:2px;background:var(--ink)}
.card{width:200px}
.card .img{width:200px;height:100px;border:3px solid #fff;box-shadow:0 1px 3px rgba(0,0,0,.2)}
.card p{font-size:11px;line-height:15px;color:var(--muted);margin:12px 0 10px}
.btn-read{width:76px;height:22px;background:var(--charcoal);color:#fff;font-size:10px;display:flex;align-items:center;justify-content:center;border-radius:2px}

/* sizes */
.tabs{left:240px;top:1396px;width:720px;display:flex;font-size:30px;color:var(--ink)}
.tabs div{flex:1;text-align:center;padding:6px 0;}
.tabs .on{color:var(--teal);background:var(--sand)}
.panel{left:240px;top:1440px;width:720px;height:276px;background:var(--sand);box-shadow:0 6px 14px rgba(0,0,0,.15)}
.size-card{width:200px;background:#fff}
.size-card .img{width:200px;height:96px;background:linear-gradient(#b8242a,#e9e2da)}
.price{left:18px;top:86px;width:52px;height:18px;background:var(--orange);color:#fff;font-size:10px;display:flex;align-items:center;justify-content:center}
.size-card p{font-size:10px;line-height:14px;color:var(--muted);padding:16px 12px 8px}
.btn-order{margin:0 0 10px 12px;width:80px;height:24px;background:var(--sand-dark);font-size:11px;display:flex;align-items:center;justify-content:center;border-radius:2px}

/* map */
.map{left:40px;top:1748px;width:1120px;height:212px;background:linear-gradient(120deg,#e8e4da,#d4e4c8 50%,#e6e1d6)}
.contact{left:352px;top:1852px;width:270px;height:104px;background:#fff;border-top:4px solid var(--orange);padding:8px 12px;font-size:11px;line-height:17px}
.contact h4{color:var(--orange);font-size:13px;margin-bottom:2px}
.contact div{display:flex;gap:6px;align-items:flex-start}
.contact i{width:10px;height:10px;border-radius:50%;background:var(--orange);margin-top:4px;flex:none}
.map-label{left:672px;top:1888px;height:36px;padding:0 14px;background:var(--charcoal);color:#fff;font-weight:900;font-size:14px;display:flex;align-items:center;letter-spacing:1px}

/* footer */
.fcol{top:2030px}
.fcol h5{font-size:22px;font-weight:900;margin-bottom:12px}
.fcol li{list-style:none;font-size:18px;line-height:26px;display:flex;align-items:center;gap:8px}
.fcol li b{width:16px;height:16px;background:var(--teal);display:block;border-radius:2px}
.blog{display:flex;gap:10px;margin-bottom:14px}
.blog .thumb{width:44px;height:44px;background:#c9b9a8}
.blog .t{font-size:11px;color:var(--orange)}
.blog .d{font-size:10px;color:var(--muted)}
.field{width:170px;height:26px;border:1px solid var(--line);font-size:12px;color:#999;padding:5px 8px;margin-bottom:8px}
.submit{width:70px;height:26px;background:var(--orange);color:#fff;font-size:12px;display:flex;align-items:center;justify-content:center}
.bottom{left:0;top:2288px;width:1200px;height:64px;background:var(--footer-bar);color:#ddd;font-size:13px;display:flex;align-items:center;justify-content:center}
</style>
</head>
<body>

<header>
  <div class="abs topbar"></div>
  <div class="abs social"><span></span><span></span><span></span><span></span></div>
  <div class="abs account"><span>Log in</span><span>Register</span></div>
  <div class="abs search">Search<b></b></div>

  <div class="abs brand"><span class="brand-dot"></span><span class="brand-name">Coral Pillow Depot</span></div>

  <nav class="abs nav">
    <span class="active">Home</span><span>Products</span><span>Prices</span><span>About Us</span><span>Contact Us</span>
  </nav>
</header>

<section>
  <div class="abs hero" role="img" aria-label="Photo of a furnished bedroom with a made-up bed and side lamps"></div>
  <p class="abs hero-copy">Lorem ipsum dolor sit amet, consectetur adipiscing elit. Nullam felis mauris</p>
  <div class="abs btn-shop">Shop now</div>
  <svg class="abs arrow" style="left:8px;top:480px" viewBox="0 0 40 40"><path d="M26 8 L12 20 L26 32" stroke="#fff" stroke-width="5" fill="none"/></svg>
  <svg class="abs arrow" style="left:1152px;top:480px" viewBox="0 0 40 40"><path d="M14 8 L28 20 L14 32" stroke="#fff" stroke-width="5" fill="none"/></svg>
  <div class="abs dots"><span></span><span></span><span class="on"></span><span></span></div>
</section>

<section>
  <div class="abs featured"></div>
  <h2 class="abs section-title" style="top:720px">Featured Products</h2>
  <div class="abs rule" style="left:300px;top:756px;width:110px"></div>
  <div class="abs rule" style="left:790px;top:756px;width:110px"></div>

  <div class="abs card" style="left:180px;top:836px">
    <div class="img" role="img" aria-label="Photo of a wooden bed frame with mattress" style="background:linear-gradient(#e9e4dc,#b88e62)"></div>
    <p>Plush pillow top with cooling gel foam layers for deep restful sleep every night.</p>
    <div class="btn-read">Read more...</div>
  </div>
  <div class="abs card" style="left:500px;top:836px">
    <div class="img" role="img" aria-label="Photo of a white quilted mattress" style="background:linear-gradient(#f5f5f5,#c7c9cc)"></div>
    <p>Quilted innerspring mattress built with reinforced edges for lasting firm support.</p>
    <div class="btn-read">Read more...</div>
  </div>
  <div class="abs card" style="left:820px;top:836px">
    <div class="img" role="img" aria-label="Photo of an upholstered bed with mattress" style="background:linear-gradient(#ece7df,#a88a6c)"></div>
    <p>Hybrid memory foam bed that relieves pressure points and keeps the body aligned.</p>
    <div class="btn-read">Read more...</div>
  </div>
  <svg class="abs arrow" style="left:76px;top:940px" viewBox="0 0 40 40"><path d="M26 8 L12 20 L26 32" stroke="#999" stroke-width="4" fill="none"/></svg>
  <svg class="abs arrow" style="left:1076px;top:940px" viewBox="0 0 40 40"><path d="M14 8 L28 20 L14 32" stroke="#999" stroke-width="4" fill="none"/></svg>
</section>

<section>
  <h2 class="abs section-title" style="top:1292px">Browse by size</h2>
  <div class="abs rule" style="left:330px;top:1328px;width:110px"></div>
  <div class="abs rule" style="left:760px;top:1328px;width:110px"></div>
  <div class="abs tabs"><div class="on">King</div><div>Queen</div><div>Full</div><div>Twin</div></div>
  <div class="abs panel"></div>

  <div class="abs size-card" style="left:360px;top:1480px">
    <div class="img" role="img" aria-label="Photo of a king bed with red bedding"></div>
    <div class="abs price">$ 549</div>
    <p>Firm support coil mattress at almost half the store price.</p>
    <div class="btn-order">Order now</div>
  </div>
  <div class="abs size-card" style="left:600px;top:1480px">
    <div class="img" role="img" aria-label="Photo of a king bed with red bedding"></div>
    <div class="abs price">$ 699</div>
    <p>Plush king pillow top delivered free across South Florida.</p>
    <div class="btn-order">Order now</div>
  </div>
  <svg class="abs arrow" style="left:226px;top:1560px" viewBox="0 0 40 40"><path d="M24 10 L14 20 L24 30" stroke="#999" stroke-width="4" fill="none"/></svg>
  <svg class="abs arrow" style="left:934px;top:1560px" viewBox="0 0 40 40"><path d="M16 10 L26 20 L16 30" stroke="#999" stroke-width="4" fill="none"/></svg>
</section>

<section>
  <div class="abs map" role="img" aria-label="Street map of the store area in Miami"></div>
  <div class="abs contact">
    <h4>Contact Us</h4>
    <div><i></i><span>4721 sw Heron Glade Ave, Miami FL 33190</span></div>
    <div><i></i><span>(786)555-0147</span></div>
    <div><i></i><span>info@coralpillowdepot.com</span></div>
  </div>
  <svg class="abs" style="left:628px;top:1872px" width="44" height="60" viewBox="0 0 44 60"><path d="M22 2 C10 2 2 11 2 22 C2 36 22 58 22 58 C22 58 42 36 42 22 C42 11 34 2 22 2Z" fill="#e0665a"/><circle cx="22" cy="22" r="8" fill="#fff"/></svg>
  <div class="abs map-label">CORAL PILLOW DEPOT</div>
</section>

<footer>
  <div class="abs fcol" style="left:130px">
    <h5>QUICK LINKS</h5>
    <ul><li>Lorem ipsum</li><li>Dolor sit amet</li><li>Consectetur</li><li>Adipiscing elit</li></ul>
  </div>
  <div class="abs fcol" style="left:380px">
    <h5>FOLLOW US</h5>
    <ul><li><b></b>Friendwall</li><li><b></b>Chirpline</li><li><b></b>Snapgrid</li><li><b></b>Pinboardly</li></ul>
  </div>
  <div class="abs fcol" style="left:600px">
    <h5>LATEST BLOG</h5>
    <div class="blog"><div class="thumb" role="img" aria-label="Blog post thumbnail photo"></div><div><div class="t">How to pick firmness</div><div class="d">March 12, 2015</div></div></div>
    <div class="blog"><div class="thumb" role="img" aria-label="Blog post thumbnail photo"></div><div><div class="t">Caring for your new bed</div><div class="d">March 04, 2015</div></div></div>
  </div>
  <div class="abs fcol" style="left:880px">
    <h5>SIGN UP TO OUR<br>NEWSLETTER</h5>
    <div class="field">Name</div>
    <div class="field">Email</div>
    <div class="submit">Submit</div>
  </div>
  <div class="abs bottom">Copyright 2015 Coral Pillow Depot. All Rights Reserved.</div>
</footer>

</body>
</html>
```